Skincare at Your Door Logo and business card

We provide dermatological services to the community. This includes Assisted Living Facilities, nursing homes and to large cooperation, Health fairs etc. We provide a health care provider that travels to institutions, providing these services. All procedures and surgeries are done onsite in one of our state of the art mobile clinics. We provide services including, but not limited to; skin biopsies, skin surgeries , surgical procedures including skin cancer removal mole removal and treatment of various skin disorders. we bring mobile Dermatology to you.

Industry/Entity Type

Business

Contact Information for Business Card

Need Logo address phone number, email website

Logo Text

Skincare at Your Door

Logo styles of interest
Emblem Logo
Abstract Logo
Character Logo
Lettermark Logo
Requirements
Must have
• Marcus Hadley ARNP DN-C
• Medical Facilitator
• P. (512) 384-9051
• Fax (619) 532-7140

```html
<!DOCTYPE html>
<html lang="en">
<head>
<meta charset="utf-8">
<title>Skincare at Your Door – Logo and Business Card</title>
<link rel="stylesheet" href="https://fonts.googleapis.com/css2?family=Arimo:wght@400;700&display=swap">
<style>
  :root {
    --brand-blue: #1f4fa6;
    --band-blue: #2a63b8;
    --band-light: #4f86cc;
    --text-dark: #2b2b2b;
    --card-white: #ffffff;
    --stage-top: #f4f4f4;
    --stage-bottom: #d9d9d9;
    --sheen-a: #c9d3d6;
    --sheen-b: #a9c4c8;
    --sheen-c: #dfe6e3;
  }
  * { margin: 0; padding: 0; box-sizing: border-box; }
  html, body { width: 1200px; height: 525px; overflow: hidden; }
  body {
    font-family: "Arimo", Arial, sans-serif;
    background: linear-gradient(180deg, var(--stage-top) 0%, var(--stage-bottom) 100%);
    position: relative;
  }
  .business-card {
    position: absolute;
    left: 60px; top: 66px;
    width: 591px; height: 368px;
    background: var(--card-white);
    box-shadow: 0 3px 10px rgba(0,0,0,0.35);
    overflow: hidden;
  }
  .card-art { position: absolute; inset: 0; }
  .brand-lockup {
    position: absolute;
    display: flex; align-items: center;
    color: var(--brand-blue);
    font-weight: 700;
    white-space: nowrap;
  }
  .brand-name { display: flex; flex-direction: column; line-height: 1.05; }
  .brand-line { display: block; }
  .brand-mark {
    border-radius: 50%;
    border: 3px solid var(--brand-blue);
    flex: none;
  }
  .card-brand { left: 34px; top: 58px; gap: 8px; font-size: 18px; }
  .card-brand .brand-mark { width: 34px; height: 34px; }
  .card-details {
    position: absolute;
    left: 333px; top: 186px;
    color: var(--text-dark);
  }
  .holder-name { font-size: 25px; font-weight: 400; color: var(--brand-blue); letter-spacing: 0.5px; }
  .credentials { font-size: 14px; color: var(--brand-blue); margin: 4px 0 0 40px; }
  .role { font-size: 14px; margin-top: 8px; letter-spacing: 0.3px; }
  .contact-lines { margin-top: 24px; display: grid; grid-template-columns: 34px auto; align-items: center; row-gap: 2px; }
  .contact-label { font-size: 9px; color: var(--text-dark); text-align: center; }
  .contact-value { font-size: 17px; color: var(--brand-blue); }
  .phone-icon { width: 20px; height: 20px; justify-self: center; }
  .stage-brand { left: 688px; top: 200px; gap: 16px; font-size: 38px; }
  .stage-brand .brand-mark { width: 72px; height: 72px; border-width: 5px; }
</style>
</head>
<body>
  <section class="business-card" aria-label="Business card">
    <svg class="card-art" viewBox="0 0 591 368" width="591" height="368">
      <defs>
        <linearGradient id="sheen" x1="0" y1="0" x2="1" y2="0">
          <stop offset="0" stop-color="var(--sheen-a)"/>
          <stop offset="0.35" stop-color="var(--sheen-b)"/>
          <stop offset="0.7" stop-color="var(--sheen-c)"/>
          <stop offset="1" stop-color="var(--sheen-a)"/>
        </linearGradient>
      </defs>
      <rect class="sheen-fill" width="591" height="368" fill="url(#sheen)" role="img" aria-label="Holographic striped foil texture"/>
      <path class="logo-field" d="M0 0 H390 C300 95 160 140 0 140 Z" fill="#fff"/>
      <path class="text-field" d="M591 118 C420 128 265 205 175 368 H591 Z" fill="#fff"/>
      <path class="top-band" d="M0 148 C160 148 300 95 398 0" stroke="var(--band-blue)" stroke-width="16" fill="none"/>
      <path class="top-band-thin" d="M0 170 C180 168 330 105 445 0" stroke="var(--band-light)" stroke-width="5" fill="none"/>
      <path class="lower-band" d="M175 368 C265 205 420 126 591 116" stroke="var(--band-blue)" stroke-width="14" fill="none"/>
      <path class="lower-band-thin" d="M150 368 C245 190 410 106 591 94" stroke="var(--band-light)" stroke-width="4" fill="none"/>
    </svg>

    <div class="brand-lockup card-brand">
      <span class="brand-mark"></span>
      <span class="brand-name"><span class="brand-line">Skincare at</span><span class="brand-line">Your Door</span></span>
    </div>

    <div class="card-details">
      <p class="holder-name">MARCUS HADLEY</p>
      <p class="credentials">ARNP DN-C</p>
      <p class="role">MEDICAL FACILITATOR</p>
      <div class="contact-lines">
        <svg class="phone-icon" viewBox="0 0 24 24" aria-label="Phone">
          <circle cx="12" cy="12" r="11" fill="none" stroke="var(--brand-blue)" stroke-width="1.6"/>
          <path d="M8 6.5c-1 .6-1.5 1.6-1.2 2.8.8 3.3 3.4 6.3 6.8 7.7 1.2.5 2.3.1 3-.8l-2.2-2c-.4.4-1 .5-1.5.2-1.3-.8-2.4-2-3-3.3-.2-.5 0-1.100.4-1.4Z" fill="var(--brand-blue)"/>
        </svg>
        <span class="contact-value">(512) 384-9051</span>
        <span class="contact-label">FAX</span>
        <span class="contact-value">(619) 532-7140</span>
      </div>
    </div>
  </section>

  <div class="brand-lockup stage-brand">
    <span class="brand-mark"></span>
    <span class="brand-name"><span class="brand-line">Skincare at</span><span class="brand-line">Your Door</span></span>
  </div>
</body>
</html>
```